Private London College Prospectus

A single spread to begin with followed by treatments for a couple of awkward spreads in the brochure. Attached docs include previous few years to show how the design has evolved. We're now looking for a different direction
Outline: Private college in Central London.
Mainly A-levels but also GCSE courses
Consistently at the top of London results table
Operated by the owners
Prospectus is sent to anyone enquiring about the college

Target Market(s)

High net worth families in the Uk and abroad

Industry/Entity Type

College

Requirements
Must have
• Modern fonts
• House colour is purple - PMS 8804
• Teacher quote
• Page quote
Nice to have
• See attachments - the gryphon is part of their logo but not essential
Should not have
• Shouldn't be too fussy or cluttered
• No script fonts (probably) no italics in main text

```html
<!DOCTYPE html>
<html lang="en">
<head>
<meta charset="utf-8">
<title>Ashcombe College Prospectus – Pages 06–07</title>
<link rel="stylesheet" href="https://fonts.googleapis.com/css2?family=Montserrat:wght@200;500&family=Open+Sans:wght@300;400;600;700&display=swap">
<style>
  :root{
    --purple:#553b7c;
    --grey-band:#d2d2d6;
    --grey-text:#6b6b6b;
    --ink:#2b2b2b;
    --paper:#ffffff;
  }
  *{box-sizing:border-box;margin:0;padding:0}
  html,body{width:1200px;height:849px;overflow:hidden;background:var(--paper)}
  body{font-family:"Open Sans",sans-serif;color:var(--ink);position:relative}
  .abs{position:absolute}

  /* left page */
  .hero-photo{left:0;top:0;width:600px;height:445px;
    background:linear-gradient(160deg,#e8d6bd 0%,#c9a27a 45%,#7b6a5c 75%,#3d4a63 100%)}
  .corner-wedge{left:0;top:0}
  .title-band{left:0;top:445px;width:600px;height:145px;background:var(--purple)}
  .title-band h1{position:absolute;left:31px;top:13px;color:#fff;font-family:"Montserrat",sans-serif;font-weight:500;font-size:29px;white-space:nowrap}
  .title-band .thin{position:absolute;left:30px;top:45px;color:#fff;font-family:"Montserrat",sans-serif;font-weight:200;font-size:50px;letter-spacing:-.3px;white-space:nowrap}
  .grey-strip{left:0;top:592px;width:600px;height:10px;background:var(--grey-band)}
  .lab-frame{left:38px;top:556px;width:228px;height:216px;background:#fff;padding:14px 14px 0}
  .lab-frame .photo{width:200px;height:200px;background:linear-gradient(170deg,#6f9468 0%,#e9e6e2 30%,#cfc8c2 70%,#9a8f88 100%)}
  .ethos{left:302px;top:655px;width:267px}
  .ethos h2{font-weight:700;color:var(--purple);font-size:23px;letter-spacing:-.3px;white-space:nowrap}
  .ethos p{margin-top:7px;font-weight:300;font-size:13px;line-height:18.4px;letter-spacing:-.35px;color:var(--grey-text);text-align:justify}

  .folio{font-size:12px;color:#8a8a8a;top:816px}
  .folio b{color:var(--purple);font-weight:700}
  .folio-left{left:27px}
  .folio-right{left:1127px}
  .rule-left{left:88px;top:828px;width:513px;height:1px;background:#9b9b9b}

  /* right page */
  .group-shot{left:636px;top:49px}
  .why-title{left:700px;top:243px;width:184px;text-align:right;font-family:"Montserrat",sans-serif;font-weight:200;color:var(--purple);font-size:20px;line-height:28px}
  .why-copy{left:636px;top:336px;width:248px;font-size:11.2px;line-height:16.2px;letter-spacing:-.15px;text-align:justify}
  .why-copy .notch{float:left;width:64px;height:32px;shape-outside:polygon(0 0,64px 0,0 32px)}
  .why-copy p+p{margin-top:8px}

  .site-url{right:37px;top:63px;font-size:12px;font-weight:600;color:var(--purple)}
  .top-rule{left:886px;top:84px;width:314px;height:1px;background:#bdbdbd}
  .best-col{left:915px;top:100px;width:248px}
  .best-col h2{font-family:"Montserrat",sans-serif;font-weight:200;color:var(--purple);font-size:19.5px;line-height:28px;letter-spacing:-.2px}
  .best-col p{margin-top:8px;font-size:11.2px;line-height:16.2px;letter-spacing:-.15px;text-align:justify}
  .best-col h2+p{margin-top:12px}
  .library-shot{left:915px;top:520px;width:249px;height:215px;background:linear-gradient(150deg,#d9c9a8 0%,#b07c4f 35%,#6b4a38 70%,#c9b59a 100%)}

  .quote-band{left:601px;top:753px}
  .teacher-frame{left:636px;top:655px;width:139px;height:135px;background:#fff;padding:8px 8px 0}
  .teacher-frame .photo{width:123px;height:127px;background:linear-gradient(180deg,#e6e4e0 0%,#d7d3cd 55%,#a9a39b 100%)}
  .teacher-name{left:626px;top:794px;width:159px;text-align:center;color:#fff}
  .teacher-name strong{display:block;font-weight:600;font-size:12px;letter-spacing:.3px}
  .teacher-name span{display:block;font-weight:600;font-size:10px;margin-top:1px}
  .quote-mark{font-family:Georgia,serif;color:#fff;font-weight:700;font-size:36px;line-height:1}
  .quote-open{left:794px;top:756px}
  .quote-close{left:1022px;top:798px}
  .teacher-quote{left:826px;top:767px;width:300px;color:#fff;font-size:12px;line-height:15px}
  .rule-right{left:601px;top:828px;width:414px;height:1px;background:#9b9b9b}
</style>
</head>
<body>

<!-- left page -->
<div class="abs hero-photo" role="img" aria-label="Photo: a teacher leaning against the wall beside a U-shaped table of seated students in a bright classroom with posters"></div>
<svg class="abs corner-wedge" width="220" height="130" viewBox="0 0 220 130" aria-hidden="true">
  <polygon points="0,0 216,0 0,124" fill="var(--purple)"/>
</svg>

<div class="abs title-band">
  <h1>A modern college with a</h1>
  <div class="thin">traditional approach</div>
</div>
<div class="abs grey-strip"></div>

<div class="abs lab-frame">
  <div class="photo" role="img" aria-label="Photo: two students in lab coats working with microscopes"></div>
</div>

<section class="abs ethos">
  <h2>THE ASHCOMBE ETHOS</h2>
  <p>Based in the heart of Mayfair in central London, Ashcombe is a top performing independent sixth-form college, offering a broad A-level and GCSE curriculum for students from public, state and private school backgrounds.</p>
</section>

<div class="abs folio folio-left">PAGE &nbsp;|&nbsp; <b>06</b></div>
<div class="abs rule-left"></div>

<!-- right page -->
<svg class="abs group-shot" width="250" height="292" viewBox="0 0 250 292" role="img" aria-label="Photo: a group of five smiling students standing together outside the college">
  <defs>
    <linearGradient id="groupTone" x1="0" y1="0" x2="1" y2="1">
      <stop offset="0" stop-color="#2f3a2e"/>
      <stop offset=".5" stop-color="#4a4f5e"/>
      <stop offset="1" stop-color="#1f2230"/>
    </linearGradient>
  </defs>
  <polygon points="0,0 250,0 250,142 0,289" fill="url(#groupTone)"/>
  <polygon points="0,289 250,142 250,152 6,292 0,292" fill="var(--purple)"/>
</svg>
<div class="abs why-title">Why<br>Choose<br>Ashcombe?</div>

<div class="abs why-copy">
  <div class="notch"></div>
  <p>The majority of students who come to Ashcombe do so because of our reputation for excellent A-level and GCSE results. This is true of students both on our full two-year programme, as well as those on the one-year intensive programme. Most students will progress on to a top 20 UK university.</p>
  <p>Students are taught very much by traditional methods, in small groups, concentrating on the skills needed to pass examinations and to be successful at university. All teachers at Ashcombe are subject specialists and most have experience as examiners. They are particularly successful with young people: they are able to motivate and communicate with them in ways which they understand. Barriers are quickly broken down, enhancing the learning process.</p>
</div>

<div class="abs site-url">www.ashcombe.org.uk</div>
<div class="abs top-rule"></div>

<section class="abs best-col">
  <h2>How Do We Get The Best Out Of Our Students?</h2>
  <p>Students benefit from individually tailored attention outside of classes – a key element of our successful A-level and GCSE programmes, and at Ashcombe each student has a Curriculum Manager and a Personal Tutor, who provide advice on study skills, subject choices and careers, and who also monitor progress in regular meetings with students.</p>
  <p>We expect full commitment from our students and as such we have strict rules on attendance and timely submission of assignments. Parents are able to monitor progress through monthly reports, easily accessible using our online reporting system. Parents’ Evenings are held during the Autumn and Spring terms.</p>
  <p>We encourage our students every step of the way and we help them to build confidence through examination success. We see the learning process as a successful partnership between students, tutors and parents.</p>
</section>
<div class="abs library-shot" role="img" aria-label="Photo: a student reading at a desk in the college library with bookshelves behind"></div>

<svg class="abs quote-band" width="599" height="96" viewBox="0 0 599 96" aria-hidden="true">
  <polygon points="0,0 599,0 599,6 409,96 0,96" fill="var(--purple)"/>
  <polygon points="599,6 599,26 452,96 409,96" fill="var(--grey-band)"/>
</svg>
<div class="abs rule-right"></div>

<div class="abs teacher-frame">
  <div class="photo" role="img" aria-label="Portrait photo of the Head of Economics"></div>
</div>
<div class="abs teacher-name"><strong>ROHAN MEHTA</strong><span>Head of Economics</span></div>

<div class="abs quote-mark quote-open">&ldquo;</div>
<p class="abs teacher-quote">We teach students how to develop their powers of analysis and independence of thought - crucial to success at university and beyond.</p>
<div class="abs quote-mark quote-close">&rdquo;</div>

<div class="abs folio folio-right">PAGE &nbsp;|&nbsp; <b>07</b></div>

</body>
</html>
```